Christmas Ballet Poster for El Relojero

I urgently need a poster for the El Relojero ballet, it needs to look magical and very similar to the reference attached. The title should be El Relojero and the typography and look should be as similar as possible as the words The Glassblower in the reference attached. Use a dancers photo just for reference, I will not use that photo as someone will be taking the picture of the principal dancer and we will be using that. It should look magical, upscale and pretty.
Requirements
Must have
- Title: El Relojero
- Space for date, time and prices
- Space to add logo
- It must look as similar as the reference as possible, magical, elegant.
Should not have
- Any logo

```html
<!DOCTYPE html>
<html lang="es">
<head>
<meta charset="utf-8">
<title>El Relojero – Ballet Ticket</title>
<link rel="stylesheet" href="https://fonts.googleapis.com/css2?family=Uncial+Antiqua&family=Cinzel:wght@400;600&family=Marcellus&display=swap">
<style>
  :root {
    --backdrop: #bfbfbf;
    --night: #04061a;
    --deep-blue: #0d1650;
    --royal-blue: #1f3590;
    --wash-blue: #2c47a8;
    --ice: #6db4e8;
    --ice-light: #a9d8f7;
    --costume: #e9e6df;
    --glow: rgba(150, 210, 255, 0.75);
  }
  * { margin: 0; padding: 0; box-sizing: border-box; }
  html, body {
    width: 1200px;
    height: 1200px;
    overflow: hidden;
    background: var(--backdrop);
  }
  .ticket {
    position: absolute;
    left: 102px;
    top: 353px;
    width: 1008px;
    height: 489px;
    overflow: hidden;
    background: linear-gradient(90deg, var(--deep-blue) 0%, #0a1240 48%, var(--night) 70%, var(--night) 100%);
  }
  .stage-backdrop {
    position: absolute;
    left: 0;
    top: 0;
    width: 760px;
    height: 489px;
    background:
      radial-gradient(ellipse 160px 70px at 120px 60px, rgba(120, 150, 225, 0.45), transparent 80%),
      radial-gradient(ellipse 200px 80px at 380px 50px, rgba(110, 140, 220, 0.35), transparent 80%),
      radial-gradient(ellipse 180px 90px at 260px 180px, rgba(100, 130, 215, 0.35), transparent 80%),
      radial-gradient(ellipse 220px 110px at 500px 230px, rgba(80, 110, 200, 0.30), transparent 80%),
      radial-gradient(ellipse 200px 90px at 420px 380px, rgba(70, 100, 190, 0.28), transparent 80%),
      radial-gradient(ellipse 150px 70px at 560px 120px, rgba(90, 120, 205, 0.25), transparent 80%),
      linear-gradient(90deg, var(--royal-blue) 0%, var(--wash-blue) 30%, #1a2a78 60%, rgba(10, 18, 64, 0) 100%);
  }
  .dancers-photo {
    position: absolute;
    left: 0;
    top: 91px;
    width: 410px;
    height: 398px;
    background:
      radial-gradient(ellipse 90px 80px at 170px 150px, rgba(240, 236, 228, 0.85), transparent 85%),
      radial-gradient(ellipse 70px 120px at 330px 290px, rgba(230, 228, 222, 0.75), transparent 85%),
      radial-gradient(ellipse 50px 150px at 90px 200px, rgba(225, 200, 190, 0.45), transparent 85%),
      radial-gradient(ellipse 200px 190px at 210px 220px, rgba(200, 205, 225, 0.25), transparent 90%);
  }
  .logo-slot {
    position: absolute;
    left: 790px;
    top: 26px;
    font-family: "Marcellus", serif;
    font-size: 46px;
    letter-spacing: 1px;
    color: var(--ice);
  }
  .title {
    position: absolute;
    left: 322px;
    top: 176px;
    line-height: 1;
    white-space: nowrap;
    font-family: "Uncial Antiqua", serif;
    font-weight: 400;
    color: var(--ice);
    text-shadow: 0 0 6px var(--glow), 0 0 14px rgba(120, 190, 255, 0.45);
  }
  .title-article {
    font-size: 58px;
    vertical-align: 28px;
    margin-right: 16px;
    color: var(--ice-light);
  }
  .title-name {
    font-size: 106px;
    letter-spacing: 0;
  }
  .date-time {
    position: absolute;
    left: 792px;
    top: 320px;
    font-family: "Cinzel", serif;
    font-weight: 600;
    font-size: 22px;
    letter-spacing: 1px;
    color: var(--ice);
  }
  .price {
    position: absolute;
    left: 834px;
    top: 388px;
    font-family: "Cinzel", serif;
    font-weight: 400;
    font-size: 46px;
    letter-spacing: 2px;
    color: var(--ice);
  }
</style>
</head>
<body>
  <main class="ticket">
    <div class="stage-backdrop" role="img" aria-label="Blue watercolour snowy stage backdrop"></div>
    <div class="dancers-photo" role="img" aria-label="Photograph of the principal ballerina in a white tutu in arabesque, partnered by a kneeling dancer in white"></div>
    <div class="logo-slot">LOGO</div>
    <h1 class="title"><span class="title-article">EL</span><span class="title-name">Relojero</span></h1>
    <div class="date-time">DATE @TIME</div>
    <div class="price">0000</div>
  </main>
</body>
</html>
```